RWT General Contracting

Roofing, Siding,windows, doors, Gutter,additions, decks, garagesand hanyman services fully insured and licensed, free estimates, accept all major credit cards call (617)442-9073 email morvinkt@mailbrook.net

Target Market(s)

Home improvement

Industry/Entity Type

Home Improvement

Requirements
Must have
• Whats listed above
Nice to have
• I dont have a logo i want wording for roofing, siding, gutter, decks, additions, windows, doors, and handyman services with my phone # 617-442-9073 and email morvinkt@mailbrook.net

```html
<!DOCTYPE html>
<html lang="en">
<head>
<meta charset="utf-8">
<title>RWT General Contracting – Postcard</title>
<link href="https://fonts.googleapis.com/css2?family=Oswald:wght@500;600;700&family=Lato:ital,wght@0,400;0,700;1,400;1,900&display=swap" rel="stylesheet">
<style>
  :root{
    --red:#e41e26;
    --charcoal:#2b2b2b;
    --ink:#2a2a2a;
    --white:#ffffff;
    --paper:#f4f4f4;
    --stage:#ececec;
    --stamp:#c9c9c9;
  }
  *{box-sizing:border-box;margin:0;padding:0}
  html,body{width:825px;height:1200px;overflow:hidden}
  body{background:var(--stage);position:relative;font-family:"Lato",Arial,sans-serif}

  .card{position:absolute;left:135px;width:568px;height:440px;overflow:hidden;background:var(--paper)}
  .card--front{top:125px}
  .card--back{top:663px;background:linear-gradient(180deg,#ffffff 0%,#f6f6f6 60%,#ededed 100%)}

  /* front */
  .front-bg{position:absolute;inset:0;background:linear-gradient(180deg,#3b3b3b 0%,#4a4a4a 28%,#cfcfcf 42%,#f1f1f1 68%,#ececec 100%)}
  .front-top-band{position:absolute;left:0;top:0;width:568px;height:30px}
  .brand-title{position:absolute;font-family:"Oswald",Impact,sans-serif;font-weight:700;color:var(--white);text-transform:uppercase;line-height:1.12;
    text-shadow:2px 0 0 var(--red),-2px 0 0 var(--red),0 2px 0 var(--red),0 -2px 0 var(--red),2px 2px 0 var(--red),-2px -2px 0 var(--red),2px -2px 0 var(--red),-2px 2px 0 var(--red)}
  .card--front .brand-title{left:32px;top:60px;font-size:35px;letter-spacing:-.3px}
  .badge-licensed{position:absolute;left:20px;top:180px;width:226px;height:38px;background:var(--red);border:2px solid var(--white);border-radius:0 20px 20px 20px;
    color:var(--white);font-family:"Oswald",sans-serif;font-weight:500;font-size:14px;display:flex;align-items:center;justify-content:center}
  .service-list{position:absolute;left:42px;top:241px;display:grid;grid-template-columns:82px auto;list-style:none;font-size:16px;color:var(--ink);line-height:20px}
  .service-list li{position:relative;padding-left:14px}
  .service-list li::before{content:"";position:absolute;left:0;top:6px;width:9px;height:9px;border-radius:50%;background:var(--red)}
  .service-list .service-free{font-weight:700;color:var(--red)}
  .call-line{position:absolute;font-family:"Oswald",sans-serif;font-weight:600}
  .card--front .call-line{left:42px;top:340px;font-size:29px;color:var(--ink)}
  .call-line .label{color:var(--red)}
  .visit-bar{position:absolute;left:0;bottom:0;width:568px;height:47px}
  .visit-lead{position:absolute;left:28px;bottom:11px;font-style:italic;font-weight:900;font-size:18px;color:var(--white);
    text-shadow:1px 1px 0 var(--red),-1px -1px 0 var(--red),1px -1px 0 var(--red),-1px 1px 0 var(--red)}
  .visit-url{position:absolute;left:204px;bottom:12px;font-style:italic;font-size:17px;color:var(--white)}
  .hero-circle{position:absolute;left:0;top:0;width:568px;height:440px}

  /* back */
  .info-panel{position:absolute;left:0;top:0;width:275px;height:364px;background:var(--charcoal);border-right:5px solid var(--red);border-bottom:5px solid var(--red)}
  .card--back .brand-title{left:28px;top:14px;font-size:32px;letter-spacing:-.3px}
  .service-band{position:absolute;left:0;top:104px;width:270px;height:150px;background:var(--red);border-top:3px solid var(--white);border-bottom:3px solid var(--white)}
  .service-band h2{position:absolute;left:23px;top:14px;font-family:"Oswald",sans-serif;font-weight:600;font-size:26px;color:var(--white);line-height:1}
  .service-band h3{position:absolute;left:23px;top:48px;font-family:"Oswald",sans-serif;font-weight:600;font-size:17px;color:var(--charcoal);line-height:1}
  .cards-note{position:absolute;left:23px;top:87px;font-family:"Oswald",sans-serif;color:var(--white);line-height:1.1}
  .cards-note strong{display:block;font-weight:500;font-size:15px}
  .cards-note span{font-size:10px;font-weight:500}
  .payment-tag{position:absolute;left:117px;top:86px;width:54px;height:36px;background:var(--charcoal);border:2px solid var(--white);border-radius:4px;
    display:flex;align-items:center;justify-content:center;color:var(--white);font-family:"Oswald",sans-serif;font-weight:500;font-size:11px}
  .contact-block{position:absolute;left:23px;top:272px;font-family:"Oswald",sans-serif;color:var(--white)}
  .contact-block .email{font-size:17px;font-weight:500}
  .card--back .call-line{position:static;font-size:27px;color:var(--white);margin-top:2px}
  .card--back .call-line .label{color:var(--white)}
  .back-circle{position:absolute;left:180px;top:90px;width:180px;height:180px}
  .stamp-box{position:absolute;left:477px;top:21px;width:67px;height:65px;background:var(--stamp)}
</style>
</head>
<body>

<section class="card card--front" aria-label="Postcard front">
  <div class="front-bg" role="img" aria-label="House siding background"></div>
  <svg class="front-top-band" viewBox="0 0 568 30" aria-hidden="true">
    <rect width="568" height="30" fill="var(--red)"/>
    <polygon points="410,0 568,0 568,30 385,30" fill="var(--charcoal)"/>
  </svg>

  <h1 class="brand-title">RWT General<br>Contracting</h1>
  <div class="badge-licensed">FULLY INSURED AND LICENSED</div>
  <ul class="service-list">
    <li>Roofing</li><li>Additions</li>
    <li>Siding</li><li>Windows</li>
    <li>Gutter</li><li>Doors</li>
    <li>Decks</li><li class="service-free">Free Estimates</li>
  </ul>
  <p class="call-line"><span class="label">CALL:</span> 617-442-9073</p>

  <svg class="hero-circle" viewBox="0 0 568 440">
    <defs>
      <radialGradient id="heroFill" cx="50%" cy="40%" r="60%">
        <stop offset="0" stop-color="#9a6a55"/>
        <stop offset=".5" stop-color="#7a4a3a"/>
        <stop offset="1" stop-color="#3d4a63"/>
      </radialGradient>
    </defs>
    <circle cx="419" cy="200" r="173" fill="var(--red)"/>
    <circle cx="433" cy="198" r="151" fill="var(--white)"/>
    <circle cx="433" cy="198" r="146" fill="url(#heroFill)" role="img" aria-label="Photo of a worker on a ladder cleaning a roof gutter"/>
  </svg>

  <svg class="visit-bar" viewBox="0 0 568 47" aria-hidden="true">
    <rect width="568" height="47" fill="var(--charcoal)"/>
    <polygon points="190,0 568,0 568,47 172,47" fill="var(--red)"/>
    <polygon points="181,0 190,0 172,47 163,47" fill="var(--white)"/>
  </svg>
  <span class="visit-lead">Please visit us</span>
  <span class="visit-url">to know more at www.website.com</span>
</section>

<section class="card card--back" aria-label="Postcard back">
  <div class="info-panel">
    <h1 class="brand-title">RWT General<br>Contracting</h1>
    <div class="service-band">
      <h2>Garages and</h2>
      <h3>handyman services</h3>
      <p class="cards-note"><strong>We accept all</strong><span>major credit cards</span></p>
      <div class="payment-tag">Paycard</div>
    </div>
    <div class="contact-block">
      <p class="email">Email: morvinkt@mailbrook.net</p>
      <p class="call-line"><span class="label">CALL:</span> 617-442-9073</p>
    </div>
  </div>
  <svg class="back-circle" viewBox="0 0 180 180">
    <defs>
      <linearGradient id="backFill" x1="0" y1="0" x2="1" y2="1">
        <stop offset="0" stop-color="#c9c4b8"/>
        <stop offset=".6" stop-color="#a2342f"/>
        <stop offset="1" stop-color="#d8d2c2"/>
      </linearGradient>
    </defs>
    <circle cx="90" cy="90" r="86" fill="var(--red)"/>
    <circle cx="90" cy="90" r="74" fill="var(--white)"/>
    <circle cx="90" cy="90" r="70" fill="url(#backFill)" role="img" aria-label="Photo of a worker installing house siding"/>
  </svg>
  <div class="stamp-box" aria-label="Stamp area"></div>
</section>

</body>
</html>
```